Letterhead for small civil engineer company

We need bold and modern design for company letterhead in MS word. It needs to have company logo and company info. Somewhere in the upper right part of document needs to be space for "recever" and the documents starts with, example, "SUBJECT: CIVIL ENGINEER LETTERHEAD".

in the bottom part of document needs to be signature and date.

Company info: Veltrana d.o.o., Lipovac 15, Lipovac (Općina Brdarić), OIB 47396028154, www.veltrana.hr, info@veltrana.hr

Email of document sender needs to be somewhere if document, exapmle xyz@veltrana.hr

Target Market(s)

Civil engineer company and projects

Industry/Entity Type

Civil engineer

Font styles to use
Serif

Colors
F0912C
F2A743
F7CA91
FBE8D2
FDF5EE

Requirements
Must have
• Company logo and company info
Nice to have
• Moder and clean design
Should not have
• Too much details

```html
<!DOCTYPE html>
<html lang="hr">
<head>
<meta charset="utf-8">
<title>Veltrana d.o.o. – Letterhead</title>
<link href="https://fonts.googleapis.com/css2?family=Open+Sans:wght@400;600;700&display=swap" rel="stylesheet">
<style>
  :root {
    --orange: #e68b36;
    --orange-soft: #f2a743;
    --grey-dark: #666666;
    --ink: #3a3a3c;
    --line: #6d6d6d;
    --paper: #ffffff;
    --backdrop: #f1f1f1;
    --mist: #ecebea;
    --sign-blue: #c9cde8;
  }
  * { margin: 0; padding: 0; box-sizing: border-box; }
  html, body { width: 1038px; height: 1200px; overflow: hidden; background: var(--backdrop); }
  body { font-family: "Open Sans", sans-serif; }
  .letterhead {
    position: absolute; left: 56px; top: 0;
    width: 925px; height: 1200px;
    background: var(--paper); overflow: hidden;
  }
  .backdrop-texture {
    position: absolute; right: 0; top: 150px; width: 460px; height: 1050px;
    background: radial-gradient(ellipse at 70% 90%, var(--mist) 0%, rgba(236,235,234,0.5) 40%, rgba(255,255,255,0) 70%),
                radial-gradient(ellipse at 60% 35%, rgba(236,235,234,0.8) 0%, rgba(255,255,255,0) 55%);
  }
  .header-waves { position: absolute; left: 0; top: 0; width: 925px; height: 340px; }
  .brand {
    position: absolute; left: 66px; top: 100px;
    display: flex; align-items: center; gap: 14px;
  }
  .brand-square { width: 34px; height: 34px; background: var(--orange); }
  .brand-name { font-size: 40px; font-weight: 400; color: var(--orange); letter-spacing: 1px; }
  .brand-rule { position: absolute; left: 66px; top: 190px; width: 402px; height: 1px; background: var(--line); }
  .company-info {
    position: absolute; left: 520px; top: 48px; width: 330px;
    text-align: center; color: #fff;
  }
  .company-name { font-size: 30px; font-weight: 700; line-height: 1.2; text-shadow: 1px 1px 2px rgba(0,0,0,0.35); margin-bottom: 12px; }
  .company-address { font-size: 13.5px; line-height: 20px; }
  .company-divider { width: 190px; height: 1px; background: rgba(255,255,255,0.6); margin: 6px auto 8px; }
  .company-web { font-size: 18px; font-weight: 700; letter-spacing: 1.5px; }
  .subject { position: absolute; left: 66px; top: 313px; font-size: 22px; color: var(--ink); font-weight: 600; }
  .subject-label { color: var(--orange); font-size: 17px; font-weight: 700; margin-right: 4px; }
  .signature-area {
    position: absolute; left: 581px; top: 997px; width: 166px; height: 62px;
    background: var(--sign-blue); border-radius: 4px; opacity: 0.6;
  }
  .date-label { position: absolute; left: 592px; top: 1074px; font-size: 15px; font-weight: 700; color: var(--orange); }
</style>
</head>
<body>
  <main class="letterhead">
    <div class="backdrop-texture" role="img" aria-label="Faint grey rounded diamond shapes and sweeping curves"></div>

    <svg class="header-waves" viewBox="0 0 925 340" aria-hidden="true">
      <path d="M468,180 C470,280 545,322 625,321 C725,320 810,288 925,313 L925,140 L468,140 Z" fill="var(--grey-dark)"/>
      <path d="M441,0 C441,165 555,303 690,302 C805,300 880,192 925,166 L925,0 Z" fill="var(--paper)"/>
      <path d="M455,0 C455,152 562,289 690,287 C800,285 880,180 925,153 L925,0 Z" fill="var(--orange)"/>
    </svg>

    <div class="brand">
      <span class="brand-square"></span>
      <span class="brand-name">VELTRANA</span>
    </div>
    <div class="brand-rule"></div>

    <section class="company-info">
      <h1 class="company-name">Veltrana d.o.o.</h1>
      <p class="company-address">Lipovac 15,<br>Lipovac (Općina Brdarić)<br>OIB 47396028154<br>email: info@veltrana.hr</p>
      <div class="company-divider"></div>
      <p class="company-web">www.veltrana.hr</p>
    </section>

    <p class="subject"><span class="subject-label">SUBJECT:</span>Civil Engineer&nbsp; Letterhead</p>

    <div class="signature-area" role="img" aria-label="Handwritten signature"></div>
    <p class="date-label">Date:</p>
  </main>
</body>
</html>
```